Premium modern eliquids labels 84.5 x 80 mm

I am looking for modern graphics for the labels of a new eliquid line that will have 4 different types of eliquids. It will have a tobacco one (brown colours maybe), a fruity one (bright colours maybe), a minty one (green colours maybe) and a creamy one (beige colours maybe).
I will need one of them to see how the design is, that design will have to be adapted to the other 3 colours of the label.
The brand logo is attached. I also attached a sample of what is mandatory to write on the label, you can change size, place and font of what is written, the only thing that cannot be reduced is the yellow parts. I attach the bottle that we will use.The size of the label is 84.5 x 80 mm (base x height).

Target Market(s)

vapers

Requirements
Must have
• My project must have one of the labels.

```html
<!DOCTYPE html>
<html lang="it">
<head>
<meta charset="utf-8">
<title>Verdant Drops – Mintara Mint Leaves label</title>
<link href="https://fonts.googleapis.com/css2?family=Barlow:wght@400;600;700;800&family=Archivo+Black&display=swap" rel="stylesheet">
<style>
  :root{
    --leaf:#8cc63f;
    --lime-pale:#eefaa6;
    --lime-soft:#f5fcc8;
    --forest:#0d6b3b;
    --forest-dark:#0a5a31;
    --tag:#fbbd2c;
    --ink:#1a1a1a;
    --page:#ffffff;
  }
  *{box-sizing:border-box;margin:0;padding:0}
  html,body{width:705px;height:1200px;overflow:hidden;background:var(--page)}
  body{position:relative;font-family:"Barlow",Arial,sans-serif}
  .label{position:absolute;left:20px;top:285px;width:665px;height:631px;overflow:hidden;background:var(--lime-pale)}
  .label__band{position:absolute;left:0;top:0;width:665px;height:160px}
  .label__base{position:absolute;left:0;bottom:0;width:100%;height:7px;background:var(--leaf)}
  .brand{position:absolute;left:0;top:50px;width:100%;text-align:center;color:#fff;font-weight:800;font-size:34px;letter-spacing:2px;line-height:1}
  .brand__sub{display:block;margin-top:6px;font-size:13px;font-weight:800;letter-spacing:9px}
  .splash{position:absolute;left:194px;top:137px;width:262px;height:469px;border-radius:48% 52% 45% 55%/40% 40% 60% 60%;
    background:radial-gradient(ellipse at 50% 45%,#b6e35a 0%,#9fd545 40%,rgba(160,214,70,.35) 70%,rgba(238,250,166,0) 100%)}
  .product{position:absolute;left:180px;top:300px;width:300px;text-align:center;color:var(--forest);line-height:1}
  .product__name{font-family:"Archivo Black","Barlow",sans-serif;font-size:50px;color:var(--forest)}
  .product__flavour{display:block;font-weight:700;font-size:13px;color:var(--forest-dark);margin-top:2px}
  .panel{position:absolute;top:140px;height:466px;border:1px solid var(--forest);border-radius:12px}
  .panel--left{left:23px;width:152px}
  .panel--right{left:490px;width:152px}
  .panel h2{font-size:14px;font-weight:700;color:var(--forest);line-height:1.2}
  .panel p{font-size:13.5px;color:var(--forest);line-height:1.3;font-weight:400}
  .ingredients{position:absolute;left:12px;top:14px}
  .rule{position:absolute;height:1px;background:var(--forest)}
  .left-rule{left:5px;top:106px;width:142px}
  .vert-rule{position:absolute;left:36px;top:116px;width:1px;height:340px;background:var(--forest)}
  .panel p.legal{position:absolute;left:0;top:0;width:340px;transform-origin:0 0;transform:rotate(-90deg);color:var(--forest);font-size:12px;line-height:1.25}
  .panel p.legal--lot{left:12px;top:456px;font-weight:700;font-size:11.5px}
  .panel p.legal--maker{left:56px;top:456px}
  .legal strong{font-weight:700}
  .instructions{position:absolute;left:10px;top:14px;width:140px}
  .right-rule-1{left:12px;top:164px;width:126px}
  .right-rule-2{left:12px;top:380px;width:126px}
  .tag{position:absolute;left:23px;background:var(--tag);color:var(--ink);font-family:"Archivo Black","Barlow",sans-serif;line-height:.95}
  .tag--bin{width:94px;height:29px;font-size:13px;padding:2px 0 0 5px}
  .tag--code{width:67px;height:29px;font-size:16px;padding:6px 0 0 7px}
  .part{position:absolute;left:26px;font-size:11px;font-weight:700;color:var(--ink)}
  .icons{position:absolute;left:36px;top:395px}
  .net{position:absolute;left:0;top:441px;width:100%;text-align:center;font-weight:700;font-size:14px;color:var(--forest)}
</style>
</head>
<body>
<main class="label">
  <svg class="label__band" viewBox="0 0 665 160" aria-hidden="true">
    <path d="M0 0H665V80C620 85 585 95 540 118C480 148 400 138 330 132C260 126 220 118 170 100C120 82 60 76 0 78Z" fill="var(--leaf)"/>
  </svg>

  <h1 class="brand">VERDANT DROPS<span class="brand__sub">FLAVOUR</span></h1>

  <div class="splash" role="img" aria-label="Green liquid splash swirling with scattered fresh mint leaves"></div>

  <div class="product">
    <div class="product__name">Mintara</div>
    <span class="product__flavour">MINT LEAVES</span>
  </div>

  <section class="panel panel--left">
    <div class="ingredients">
      <h2>INGREDIENTI:</h2>
      <p>Glicole,<br>Propilenico,<br>Sostanze,<br>Aromatizzanti</p>
    </div>
    <div class="rule left-rule"></div>
    <div class="vert-rule"></div>
    <p class="legal legal--lot">L.SH20 - 001-PES-D.PROD.22-04-2022 D.SC.21-04-2024</p>
    <p class="legal legal--maker"><strong>PRODOTTO E CONFEZIONATO</strong><br>DA Fogliaverde srl, Via del Lago 18, 10100 Borgoverde,<br>P.i.00000000000<br>Tel. +39 000 1234567 | info@fogliaverde.it</p>
  </section>

  <section class="panel panel--right">
    <div class="instructions">
      <h2>ISTRUZIONI D’USO:</h2>
      <p>Agitare bene prima<br>dell’utilizzo. Diluire<br>nelle percentuali<br>consigliate sul<br>nostro sito.<br>Conservare in luogo<br>fresco e asciutto</p>
    </div>
    <div class="rule right-rule-1"></div>
    <div class="tag tag--bin" style="top:188px">RACCOLTA<br>PLASTICA</div>
    <div class="part" style="top:220px">ETICHETTA</div>
    <div class="tag tag--code" style="top:236px">PAP 5</div>
    <div class="tag tag--bin" style="top:282px">RACCOLTA<br>PLASTICA</div>
    <div class="part" style="top:315px;left:30px">FLACONE</div>
    <div class="tag tag--code" style="top:331px">PET 1</div>
    <div class="rule right-rule-2"></div>
    <svg class="icons" width="80" height="44" viewBox="0 0 80 44" aria-hidden="true" fill="none" stroke="var(--forest)" stroke-width="1.6">
      <path d="M16 8l6 10h-12z"/><path d="M4 30l6-10 6 10z"/><path d="M22 30l6-10 6 10z"/>
      <path d="M46 18h10l-2 22h-6z" stroke-width="2"/>
      <circle cx="66" cy="6" r="3.5" fill="var(--forest)" stroke="none"/>
      <path d="M62 12h8v16h-2v12h-4v-12h-2z" fill="var(--forest)" stroke="none"/>
    </svg>
    <div class="net">20 ML NET</div>
  </section>

  <div class="label__base"></div>
</main>
</body>
</html>
```